Blue Heron Business Card

This is a business card for a printing company but I actually don't have a logo. Just need to typeset the words "Blue Heron Printing" as the logo. Then add my name "Marla Vossen" + phone number + address

Target Market(s)

ceos and professionals

Industry/Entity Type

printing and manufacturing

Contact Information for Business Card

Blue Heron Printing/ 4817 dunmore ave. S. El Monte, CA 90418/ 626-447-3092/ Marla Vossen

Font styles to use
Serif
Other font styles liked:
• a modern font would be nice

Colors
0054AA
0677BA
7BADD7
CADEEF
E8F1F8
0094D4
00A9DD
6FCCEA
C7EBF8
E9F6FB

Requirements
Must have
• company name, number, address
Nice to have
• nice bold feel
Should not have
• nothing in particular

```html
<!DOCTYPE html>
<html lang="en">
<head>
<meta charset="utf-8">
<title>Blue Heron Business Card</title>
<link rel="stylesheet" href="https://fonts.googleapis.com/css2?family=Montserrat:wght@400;500;700;800&display=swap">
<style>
  :root {
    --bg: #4d4d4d;
    --card: #1a1a1c;
    --edge: #0677ba;
    --brand: #0677ba;
    --accent: #0094d4;
    --text: #e6e6e6;
    --muted: #9a9a9a;
  }
  * { margin: 0; padding: 0; box-sizing: border-box; }
  html, body { width: 1200px; height: 900px; overflow: hidden; }
  body {
    background: var(--bg);
    font-family: "Montserrat", sans-serif;
    position: relative;
  }
  .card {
    position: absolute;
    width: 560px;
    height: 320px;
    background: var(--card);
    border-radius: 22px;
    box-shadow: 0 4px 0 var(--edge), 0 14px 28px rgba(0,0,0,.45);
    overflow: hidden;
  }
  .card--front { left: 80px; top: 70px; }
  .card--back { left: 560px; top: 500px; }

  .wordmark {
    font-weight: 800;
    color: var(--brand);
    text-transform: uppercase;
    letter-spacing: -1px;
    line-height: 1;
  }
  .card--front .wordmark {
    position: absolute; left: 0; right: 0; top: 118px;
    text-align: center; font-size: 44px;
  }
  .card--front .website {
    position: absolute; left: 0; right: 0; top: 214px;
    text-align: center; font-size: 13px; color: var(--text);
  }
  .website .domain { color: var(--accent); }

  .card--back .wordmark {
    position: absolute; left: 40px; top: 44px; font-size: 36px;
  }
  .divider {
    position: absolute; left: 40px; right: 40px; top: 196px;
    height: 2px; background: var(--edge);
  }
  .person { position: absolute; left: 40px; top: 148px; }
  .person__name { font-weight: 700; font-size: 22px; color: var(--accent); }
  .person__title { font-size: 12px; color: var(--text); margin-top: 2px; }
  .address {
    position: absolute; right: 40px; top: 152px;
    text-align: right; font-size: 13px; color: var(--text); line-height: 1.45;
  }
  .contacts { position: absolute; left: 40px; top: 214px; list-style: none; }
  .contacts li {
    display: flex; align-items: center; gap: 12px;
    font-size: 13px; color: var(--text); margin-bottom: 9px;
  }
  .contacts svg { width: 14px; height: 14px; fill: var(--accent); flex: none; }
</style>
</head>
<body>
  <section class="card card--front">
    <h1 class="wordmark">Blue Heron Printing</h1>
    <p class="website">www.<span class="domain">blueheronprint</span>.com</p>
  </section>

  <section class="card card--back">
    <h2 class="wordmark">Blue Heron Printing</h2>
    <div class="person">
      <p class="person__name">Marla Vossen</p>
      <p class="person__title">Manager</p>
    </div>
    <p class="address">4817 Dunmore Ave.<br>S. El Monte, CA 90418</p>
    <div class="divider"></div>
    <ul class="contacts">
      <li>
        <svg viewBox="0 0 24 24" aria-hidden="true"><path d="M6.6 10.8a15.1 15.1 0 0 0 6.6 6.6l2.2-2.2c.3-.3.7-.4 1-.2 1.1.4 2.3.6 3.6.6.6 0 1 .4 1 1V20c0 .6-.4 1-1 1A17 17 0 0 1 3 4c0-.6.4-1 1-1h3.5c.6 0 1 .4 1 1 0 1.3.2 2.5.6 3.6.1.3 0 .7-.2 1z"/></svg>
        626-447-3092
      </li>
      <li>
        <svg viewBox="0 0 24 24" aria-hidden="true"><path d="M2 5h20v14H2z M2 5l10 8 10-8" fill="none" stroke="#0094d4" stroke-width="2"/></svg>
        info@blueheronprint.com
      </li>
      <li>
        <svg viewBox="0 0 24 24" aria-hidden="true"><circle cx="12" cy="12" r="9" fill="none" stroke="#0094d4" stroke-width="2"/><path d="M3 12h18M12 3c3 3 3 15 0 18M12 3c-3 3-3 15 0 18" fill="none" stroke="#0094d4" stroke-width="1.6"/></svg>
        www.blueheronprint.com
      </li>
    </ul>
  </section>
</body>
</html>
```